Accountancy practice needs a wordpress website redesign for growth

We are a growing accountancy practice - headcount and revenues have doubled in the last 2 years. We are continuing to grow. We only had a website made around 12 months ago but the company we used offered very little in terms of creativity and ideas of how to make it look modern and eye-catching. We want to redesign the website to make it look premium and professional because we are starting to launch more marketing and drive more traffic to the site.

The current website is www.tovelbrookaccountants.co.uk. The website was built in wordpress.

The logo has been uploaded. The main 2 colour hex codes are: 0E74BC and 14A79D.

We are open to changing the fonts in the website and welcome suggestions for this too.

Following on from this we will launch a project to design brochures and one-page flyers that we can fill with useful information about what we do and also create lead-generators to download from the website. So the design of the website will influence the overall brand and feel of all of the marketing collateral.

Target Market(s)

Property businesses and entrepreneurial, growth mindset clients

Industry/Entity Type

Accountancy

Number of Pages Required

3 page

Font styles to use
Sans Serif

Colors

Designer to choose colors to be used in the design.

Requirements
Must have
• A modern and professional feel. 3 fonts - most websites seem to use 3 different fonts now and I like this. We have our green and blue colours but I do not want too much of this all over the site, stick to blacks, whites and greys with the blue and green used for emphasis and accents.
Nice to have
• The coloured spaces should have some "depth" to them, eg a small pattern in the white spaces so its not just a solid whie background.

```html
<!DOCTYPE html>
<html lang="en">
<head>
<meta charset="utf-8">
<title>Tovelbrook Accountants – Blog</title>
<link href="https://fonts.googleapis.com/css2?family=Oswald:wght@500&family=Open+Sans:wght@400;600&display=swap" rel="stylesheet">
<style>
:root{
  --blue:#0e74bc;
  --green:#14a79d;
  --mint:#d3efec;
  --ink:#1b1f26;
  --text:#3b3f45;
  --footer:#131b25;
  --footer-text:#b6bcc4;
  --highlight:#8fc3ec;
  --white:#ffffff;
}
*{box-sizing:border-box;margin:0;padding:0}
html,body{width:1200px;height:2623px;overflow:hidden;background:var(--white)}
body{position:relative;font-family:'Open Sans',sans-serif;color:var(--text)}
.oswald{font-family:'Oswald',sans-serif;font-weight:500}

.site-header{position:absolute;top:0;left:0;width:1200px;height:76px;background:var(--white)}
.brand{position:absolute;left:66px;top:20px;display:flex;align-items:center;gap:10px}
.brand-mark{width:22px;height:22px;background:var(--blue)}
.brand-name{font-family:'Oswald',sans-serif;font-weight:500;font-size:24px;color:var(--blue);letter-spacing:1px}
.main-nav{position:absolute;top:30px;left:426px;display:flex;gap:38px;font-family:'Oswald',sans-serif;font-weight:500;font-size:12.5px;color:var(--ink);text-transform:uppercase}
.btn-head{position:absolute;top:15px;height:46px;display:flex;align-items:center;justify-content:center;color:var(--white);font-family:'Oswald',sans-serif;font-weight:500;font-size:15px;letter-spacing:.5px;border-radius:3px}
.btn-contact{left:869px;width:125px;background:var(--blue)}
.btn-login{left:1005px;width:117px;background:var(--green)}

.hero{position:absolute;top:76px;left:0;width:1200px;height:392px;background:linear-gradient(100deg,#1a2a2c 0%,#1f3f3f 40%,#2c5a56 70%,#17322f 100%)}
.hero-title{position:absolute;left:97px;top:118px;font-size:50px;line-height:56px;color:var(--white)}
.hero-title .line{display:block}
.hero-title .mark{display:inline-block;margin-top:4px;background:var(--highlight);padding:0 8px;line-height:48px;height:48px}

.intro{position:absolute;top:535px;left:0;width:1200px;text-align:center}
.intro h1{font-size:41px;color:var(--ink);line-height:58px}
.intro p{margin-top:18px;font-size:18.5px;line-height:27px;color:var(--ink)}

.card{position:absolute;width:281px}
.card-img{width:281px;height:268px}
.card h2{margin-top:26px;font-size:19.5px;line-height:26px;color:var(--ink);white-space:nowrap;letter-spacing:-.1px}
.card time{display:block;margin-top:5px;font-size:13.5px;color:var(--blue);letter-spacing:.3px}
.card p{margin-top:15px;padding-left:2px;font-size:15px;line-height:25.6px;color:var(--text)}
.read-more{position:absolute;left:0;width:135px;height:48px;display:flex;align-items:center;justify-content:center;background:var(--mint);color:var(--green);font-family:'Oswald',sans-serif;font-weight:500;font-size:15px;border-radius:2px}
.read-more.is-active{background:var(--green);color:var(--white);box-shadow:0 6px 14px rgba(20,167,157,.35)}

.pagination{position:absolute;top:2132px;left:490px;display:flex;align-items:center;gap:16px;font-size:15px;color:var(--ink);font-weight:600}
.pagination span{width:22px;text-align:center}
.pagination .current{background:var(--blue);color:var(--white);border-radius:3px;height:24px;line-height:24px}

.site-footer{position:absolute;top:2227px;left:0;width:1200px;height:396px;background:var(--footer);color:var(--footer-text)}
.footer-brand{position:absolute;left:156px;top:95px;display:flex;align-items:center;gap:10px}
.footer-brand .brand-mark{background:var(--green)}
.footer-brand .brand-name{color:var(--blue)}
.address{position:absolute;left:156px;top:160px;font-size:13.5px;line-height:20px}
.contact-line{position:absolute;left:156px;display:flex;align-items:center;gap:14px;font-size:13.5px}
.contact-line .dot{width:24px;height:24px;border-radius:50%;background:#202a36;display:flex;align-items:center;justify-content:center}
.footer-col{position:absolute;top:98px}
.footer-col h3{font-size:14.5px;color:var(--white);margin-bottom:18px}
.footer-col li{list-style:none;font-size:13.5px;line-height:29px}
.copyright{position:absolute;left:155px;top:344px;font-size:13px;white-space:nowrap}
.badge{position:absolute;top:334px;height:32px;background:#e8ecf2}
.social{position:absolute;top:334px;left:905px;display:flex;gap:9px}
.social span{width:28px;height:28px;border-radius:50%;background:#202a36}
</style>
</head>
<body>
<header class="site-header">
  <div class="brand"><span class="brand-mark"></span><span class="brand-name">TOVELBROOK</span></div>
  <nav class="main-nav"><span>About us</span><span>Who we help</span><span>Thoughts</span><span>Switching accountants</span></nav>
  <a class="btn-head btn-contact">GET IN TOUCH</a>
  <a class="btn-head btn-login">LOGIN</a>
</header>

<section class="hero" role="img" aria-label="Close-up photograph of vintage typewriter keys in dark teal tones">
  <h1 class="hero-title oswald"><span class="line">Interesting and</span><span class="mark">useful blog</span></h1>
</section>

<section class="intro">
  <h1 class="oswald">Stay up to date</h1>
  <p>Read one of our many blogs and stay up to date with everything related to<br>accounting, cash flow solutions, commercial finance and much more.</p>
</section>

<article class="card" style="left:156px;top:706px;height:640px">
  <div class="card-img" role="img" aria-label="Tablet showing colourful charts" style="background:linear-gradient(135deg,#e6ecf3,#c4d3e3)"></div>
  <h2 class="oswald">Why your startup pitch needs<br>sensitivity analysis</h2>
  <time>12 AUG, 2023</time>
  <p>It takes more than an all-star team, a product with a competitive advantage, and a sizable potential market to guarantee fundraising success for your startup. With thousands of proposals flooding investors’ inboxes each year, and venture capital facing,</p>
  <a class="read-more" style="top:594px">READ MORE</a>
</article>
<article class="card" style="left:458px;top:706px;height:640px">
  <div class="card-img" role="img" aria-label="Hand holding a paper figure stopping falling dominoes" style="background:linear-gradient(135deg,#a7714f,#8a5a3c)"></div>
  <h2 class="oswald">How Forensic Accounting Can<br>Supercharge Your Financial Risk<br>Analysis</h2>
  <time>11 AUG, 2023</time>
  <p>A few years ago, Dara Whitcombe—a forensic accounting expert at Ledgerline, who has held regional and divisional CFO roles at Corvane and Halden &amp; Reyes—was reviewing a company’s performance at the request</p>
  <a class="read-more is-active" style="top:594px">READ MORE</a>
</article>
<article class="card" style="left:765px;top:706px;height:640px">
  <div class="card-img" role="img" aria-label="Business handshake in an office" style="background:linear-gradient(135deg,#5d6d85,#c9b7a8)"></div>
  <h2 class="oswald">5 Key Tips for Smarter Sales and<br>Operations Planning Implementation</h2>
  <time>10 AUG, 2023</time>
  <p>Since 2020, a slew of disruptions has obstructed the smooth operations of companies around the world, making it difficult for many to obtain the parts they need or get their products to customers. With significant economic uncertainty likely to continue</p>
  <a class="read-more" style="top:594px">READ MORE</a>
</article>

<article class="card" style="left:156px;top:1432px;height:640px">
  <div class="card-img" role="img" aria-label="Model house with keys on architectural plans" style="background:linear-gradient(135deg,#dfe3e8,#a7574a)"></div>
  <h2 class="oswald">Real Estate Financial Modeling: 3<br>Costly Mistakes to Avoid</h2>
  <time>9 AUG, 2023</time>
  <p>The combination of inflation and rising interest rates isn’t just making homes more expensive to buy—it’s also making them more expensive to build. According to a running tally kept by the US Federal Reserve, the producer price index for construction materials rose</p>
  <a class="read-more" style="top:594px">READ MORE</a>
</article>
<article class="card" style="left:458px;top:1432px;height:640px">
  <div class="card-img" role="img" aria-label="Laptop displaying an analytics dashboard" style="background:linear-gradient(135deg,#d9d6d2,#2c3440)"></div>
  <h2 class="oswald">The KPI Cure: How Healthcare Data<br>Analytics Can Improve Medical<br>Center Finances</h2>
  <time>8 AUG, 2023</time>
  <p>US healthcare providers could collectively cut more than $1.5 trillion in costs over the next six years by implementing productivity improvements, according to a 2022 report from Marlow &amp; Finch. When it</p>
  <a class="read-more" style="top:594px">READ MORE</a>
</article>
<article class="card" style="left:765px;top:1432px;height:640px">
  <div class="card-img" role="img" aria-label="Paper with rising arrow held against skyscrapers" style="background:linear-gradient(135deg,#4f8fd0,#cfe0f0)"></div>
  <h2 class="oswald">Forensic Accounting: Due Diligence’s<br>Secret Weapon</h2>
  <time>7 AUG, 2023</time>
  <p>The term “forensic accounting” may conjure up images of detectivelike professionals scouring files, conducting interviews, and running background checks to crack cases of financial crime. While that is part of the job, forensic accountants are also needed to</p>
  <a class="read-more" style="top:594px">READ MORE</a>
</article>

<nav class="pagination">
  <span>&#8249;</span><span class="current">1</span><span>2</span><span>3</span><span>…</span><span>9</span><span>&#8250;</span>
</nav>

<footer class="site-footer">
  <div class="footer-brand"><span class="brand-mark"></span><span class="brand-name">TOVELBROOK</span></div>
  <p class="address">12 Mill Lane, Ashcombe,<br>AB1 2CD</p>
  <div class="contact-line" style="top:218px"><span class="dot"><svg width="10" height="8" viewBox="0 0 10 8"><rect x=".5" y=".5" width="9" height="7" fill="none" stroke="#b6bcc4"/><path d="M.5 .5 5 4.5 9.5 .5" fill="none" stroke="#b6bcc4"/></svg></span>info@tovelbrookaccountants.co.uk</div>
  <div class="contact-line" style="top:252px"><span class="dot"><svg width="10" height="10" viewBox="0 0 10 10"><path d="M2 1 4 3 3 4.5Q4.5 6.5 6 7L7.5 6 9.5 8 8 9.5Q3 9 .5 2Z" fill="#b6bcc4"/></svg></span>01632 960418</div>
  <div class="footer-col" style="left:462px"><h3 class="oswald">ABOUT</h3><ul><li>Meet The Team</li><li>Our Values</li><li>Software Solutions</li><li>Vacancies</li></ul></div>
  <div class="footer-col" style="left:662px"><h3 class="oswald">SERVICES</h3><ul><li>Company Services</li><li>Personal Services</li><li>Advisory Services</li></ul></div>
  <div class="footer-col" style="left:863px"><h3 class="oswald">WHO WE HELP</h3><ul><li>Property Investors and Developers</li><li>Consultants</li><li>Medical Professionals</li><li>Buying or Selling a Business</li></ul></div>
  <p class="copyright">Copyright © 2023 tovelbrookaccountants. All rights reserved</p>
  <div class="badge" style="left:560px;width:68px"></div>
  <div class="badge" style="left:652px;width:100px;background:#3a4452"></div>
  <div class="social"><span></span><span></span><span></span><span></span></div>
</footer>
</body>
</html>
```